RT Website Home Page Design

The task is to develop a winning design for a replacement website for our client RT Plumbing, Heating, AC & Remodeling. ct

```html
<!DOCTYPE html>
<html lang="en">
<head>
<meta charset="utf-8">
<title>RT Plumbing, Heating, AC &amp; Remodeling – Home</title>
<link href="https://fonts.googleapis.com/css2?family=Josefin+Sans:wght@400;600;700&family=Montserrat:wght@400;600;700&display=swap" rel="stylesheet">
<style>
:root{
  --navy:#1d3a6b;
  --navy-deep:#1b3461;
  --yellow:#f6dc16;
  --tile:#e3f2fb;
  --text:#3a3f4a;
  --muted:#6b7280;
  --light:#f4f2f2;
  --white:#fff;
}
*{box-sizing:border-box;margin:0;padding:0}
html,body{width:1200px;height:4441px;overflow:hidden}
body{font-family:"Josefin Sans",sans-serif;color:var(--text);background:var(--white);position:relative}
.abs{position:absolute}
.btn{position:absolute;background:var(--yellow);color:var(--navy);font-family:"Josefin Sans",sans-serif;font-weight:600;font-size:14px;letter-spacing:.5px;display:flex;align-items:center;justify-content:center;text-transform:uppercase;padding-top:3px}
.rule{width:36px;height:3px;background:var(--yellow)}
.heading{color:var(--navy);font-weight:700;font-size:25px;letter-spacing:1px;text-transform:uppercase}

/* header */
.site-header{position:absolute;left:0;top:0;width:1200px;height:133px;background:var(--white)}
.brand{position:absolute;left:133px;top:28px;display:flex;align-items:center;gap:10px}
.brand-dot{width:34px;height:34px;border-radius:50%;background:var(--yellow)}
.brand-name{color:var(--navy);font-weight:700;font-size:22px;line-height:1}
.serving{position:absolute;right:131px;top:28px;font-size:13px;color:var(--navy)}
.phones{position:absolute;right:131px;top:54px;font-size:18px;color:var(--navy);font-weight:600;display:flex;gap:14px;align-items:center}
.phones .sep{width:2px;height:18px;background:var(--yellow)}
.main-nav{position:absolute;left:133px;top:101px;width:938px;display:flex;justify-content:space-between;font-size:11.5px;font-weight:600;color:var(--navy);text-transform:uppercase;letter-spacing:.3px}

/* hero */
.hero{position:absolute;left:0;top:133px;width:1200px;height:491px;background:linear-gradient(90deg,#6f6a64 0%,#a79f95 40%,#d9d2c7 70%,#c8c1b6 100%)}
.hero h1{position:absolute;left:133px;top:66px;color:var(--white);font-size:40px;line-height:46px;font-weight:700;text-transform:uppercase;letter-spacing:1px}
.dots{position:absolute;left:143px;top:431px;display:flex;gap:14px}
.dots span{width:12px;height:12px;border-radius:50%;background:var(--navy)}
.dots span.on{background:var(--yellow)}

/* services */
.services-title{position:absolute;left:0;top:672px;width:1200px;text-align:center}
.services-title .rule{margin:18px auto 0}
.tiles{position:absolute;left:133px;top:758px;width:936px;display:grid;grid-template-columns:repeat(4,224px);grid-auto-rows:181px;gap:10px 13px}
.tile{background:var(--tile);display:flex;flex-direction:column;align-items:center;justify-content:flex-end;padding-bottom:38px;color:var(--navy);font-size:15px}
.tile svg{margin-bottom:22px}
.tile.active{background:var(--navy);color:var(--white);justify-content:center;padding-bottom:0}
.tile.active svg{margin-bottom:14px}
.tile .more{background:var(--yellow);color:var(--navy);font-size:9px;font-weight:700;padding:4px 7px 2px;margin-top:10px}

/* request form */
.request{position:absolute;left:0;top:1190px;width:1200px;height:565px;background:linear-gradient(90deg,var(--light) 0%,var(--light) 40%,#cfc9c4 58%,#8a8580 80%,#6c6964 100%)}
.request .heading{position:absolute;left:133px;top:38px}
.field{position:absolute;left:134px;width:328px;height:38px;background:var(--white);font-size:11px;color:#555;padding:13px 12px 0}

/* back to school */
.reminder-photo{position:absolute;left:133px;top:1803px;width:493px;height:354px;background:linear-gradient(135deg,#e6e2dc,#b9aea2 55%,#8d7a6a)}
.reminder{position:absolute;left:684px;top:1823px;width:385px}
.reminder p{font-size:16px;line-height:24px;margin-top:34px;color:var(--text)}

/* difference */
.difference{position:absolute;left:0;top:2207px;width:1200px;height:443px;background:linear-gradient(90deg,#f3f3f4,#ecedef)}
.difference .copy{position:absolute;left:133px;top:52px;width:395px}
.difference p{font-size:15.5px;line-height:24px;margin-top:30px}
.diff-photo{position:absolute;left:655px;top:43px;width:362px;height:362px;border-radius:50%;background:radial-gradient(circle at 45% 45%,#e8e9ec,#aeb6c3 60%,#2e4f8f)}

/* savings */
.savings-title{position:absolute;left:0;top:2700px;width:1200px;text-align:center}
.savings-title .rule{margin:18px auto 0}
.offer{position:absolute;top:2781px;width:297px;height:231px;padding:26px 24px}
.offer h3{font-family:"Montserrat",sans-serif;font-style:italic;color:var(--navy);font-size:18px;line-height:24px;font-weight:700}
.offer .save{display:inline-block;margin-top:10px;background:var(--navy);color:var(--white);font-family:"Montserrat",sans-serif;font-style:italic;font-weight:700;font-size:17px;padding:7px 14px}
.offer p{font-size:14.5px;line-height:19px;margin-top:12px;width:150px;color:#4a4f58}

/* blog */
.blog{position:absolute;left:0;top:3131px;width:1200px;height:657px;background:linear-gradient(180deg,#2d2e33,#1d1e22)}
.blog .heading{position:absolute;left:0;top:48px;width:1200px;text-align:center;color:var(--white)}
.blog .heading .rule{margin:16px auto 0}
.post{position:absolute;top:115px;width:292px;height:430px;background:var(--white)}
.post .img{height:196px;background:linear-gradient(135deg,#d7dde6,#7e8da6 55%,#2e4573)}
.post .body{padding:22px 24px 0}
.post .date{font-family:"Montserrat",sans-serif;font-size:11px;font-weight:700;color:#222}
.post h4{font-family:"Montserrat",sans-serif;font-size:12.5px;font-weight:700;color:#222;line-height:18px;margin-top:12px}
.post p{font-family:"Montserrat",sans-serif;font-size:10.5px;line-height:14px;color:#555;margin-top:10px}
.post .btn{left:24px;top:370px;width:86px;height:36px;font-size:12px}

/* footer */
.site-footer{position:absolute;left:0;top:3788px;width:1200px;height:653px;background:var(--navy-deep);color:#c9d2e4}
.fcol{position:absolute;width:250px}
.fcol h5{color:var(--white);font-size:12px;font-weight:700;text-transform:uppercase;letter-spacing:.4px}
.fcol .rule{width:28px;height:2px;margin:8px 0 10px}
.fcol ul{list-style:none;font-size:11.5px;line-height:19.5px}
.club{position:absolute;left:133px;top:453px;display:flex;align-items:center;gap:10px}
.club .dot{width:30px;height:30px;border-radius:50%;background:var(--yellow)}
.club span{color:var(--white);font-size:18px;font-weight:700}
.address{position:absolute;left:349px;top:454px;font-size:12px;line-height:22px}
.follow{position:absolute;left:611px;top:480px;display:flex;align-items:center;gap:14px;color:var(--white);font-size:12px;font-weight:700}
.follow i{width:34px;height:34px;border-radius:50%;background:#3d63b4;display:block}
.cards{position:absolute;left:853px;top:475px;display:flex;gap:8px}
.cards i{width:48px;height:30px;border-radius:3px;background:#fff;display:block}
.footer-line{position:absolute;left:133px;top:568px;width:936px;height:1px;background:#3c5589}
.copyright{position:absolute;left:0;top:605px;width:1200px;text-align:center;color:var(--white);font-size:11.5px}
</style>
</head>
<body>

<header class="site-header">
  <div class="brand"><div class="brand-dot"></div><div class="brand-name">RT Plumbing</div></div>
  <div class="btn" style="left:409px;top:29px;width:153px;height:40px">Request Service</div>
  <div class="btn" style="left:578px;top:29px;width:150px;height:40px">Request a Quote</div>
  <div class="serving">Serving Ashford, MA &amp; Neighboring Communities.</div>
  <div class="phones">
    <svg width="18" height="18" viewBox="0 0 24 24" fill="none" stroke="#1d3a6b" stroke-width="2"><path d="M5 3h4l2 5-3 2a12 12 0 0 0 6 6l2-3 5 2v4a2 2 0 0 1-2 2A17 17 0 0 1 3 5a2 2 0 0 1 2-2z"/></svg>
    <span>555.210.4870</span><span class="sep"></span><span>800.555.0143</span>
  </div>
  <nav class="main-nav">
    <span>About</span><span>Plumbing</span><span>Water Heaters</span><span>Heating</span><span>Air Conditioning</span><span>Indoor Air Quality</span><span>Commercial</span><span>Handy Work &amp; Remodeling</span><span>Contact</span>
  </nav>
</header>

<section class="hero" role="img" aria-label="Smiling family at home holding a cardboard roof over their heads">
  <h1>Enjoy the best<br>of home living.<br>Indoors &amp; out.</h1>
  <div class="btn" style="left:133px;top:226px;width:246px;height:44px">Contact us to get started</div>
  <div class="dots"><span></span><span class="on"></span><span></span></div>
</section>

<div class="services-title"><div class="heading">More of what you need</div><div class="rule"></div></div>
<div class="tiles">
  <div class="tile"><svg width="54" height="54" viewBox="0 0 54 54" fill="none" stroke="#1d3a6b" stroke-width="2"><path d="M10 40v-14h14v-8h8v8M24 26v14M6 40h8M40 10v10h6M36 14h8"/><circle cx="18" cy="44" r="3"/></svg>Plumbing</div>
  <div class="tile active"><svg width="44" height="54" viewBox="0 0 44 54" fill="none" stroke="#fff" stroke-width="2"><rect x="8" y="4" width="28" height="40" rx="3"/><circle cx="22" cy="20" r="6"/><path d="M14 50v-6M30 50v-6"/></svg>Water Heaters<span class="more">Read More</span></div>
  <div class="tile"><svg width="54" height="54" viewBox="0 0 54 54" fill="none" stroke="#1d3a6b" stroke-width="2"><rect x="6" y="8" width="42" height="38"/><path d="M6 18h42M6 28h42M6 38h42M18 8v38M30 8v38"/></svg>Heating</div>
  <div class="tile"><svg width="54" height="54" viewBox="0 0 54 54" fill="none" stroke="#1d3a6b" stroke-width="2"><rect x="4" y="10" width="46" height="18" rx="2"/><path d="M10 22h34M18 34c-2 4 2 6 0 10M27 34c-2 4 2 6 0 10M36 34c-2 4 2 6 0 10"/></svg>Air Conditioning</div>
  <div class="tile"><svg width="54" height="54" viewBox="0 0 54 54" fill="none" stroke="#1d3a6b" stroke-width="2"><path d="M6 20h28a5 5 0 1 0-5-5M6 28h38a5 5 0 1 1-5 5M6 36h22"/></svg>Indoor Air Quality</div>
  <div class="tile"><svg width="54" height="54" viewBox="0 0 54 54" fill="none" stroke="#1d3a6b" stroke-width="2"><rect x="8" y="14" width="10" height="32" rx="3"/><rect x="22" y="14" width="10" height="32" rx="3"/><rect x="36" y="14" width="10" height="32" rx="3"/><path d="M6 8h42v6H6z"/></svg>Water Filtration</div>
  <div class="tile"><svg width="54" height="54" viewBox="0 0 54 54" fill="none" stroke="#1d3a6b" stroke-width="2"><path d="M10 44l22-22M14 8a8 8 0 0 0 10 10l22 22-6 6-22-22A8 8 0 0 0 8 14l6 6 6-6z"/></svg>Remodeling &amp; Handy Work</div>
  <div class="tile"><svg width="54" height="54" viewBox="0 0 54 54" fill="none" stroke="#1d3a6b" stroke-width="2"><path d="M8 46V22L27 8l19 14v24z"/><rect x="16" y="26" width="22" height="16"/><path d="M27 38c-4-3 0-7 0-9 3 3 4 6 0 9z"/></svg>Gas Fireplaces</div>
</div>

<section class="request">
  <div class="abs" role="img" aria-label="White company service van parked on a city street" style="left:520px;top:0;width:680px;height:565px;background:linear-gradient(90deg,rgba(244,242,242,0) 0%,rgba(226,224,222,.5) 30%,rgba(190,188,186,.4) 60%,rgba(110,104,98,.6) 100%)"></div>
  <div class="heading">Request Service</div>
  <div class="field" style="top:96px">*Name</div>
  <div class="field" style="top:144px">Address</div>
  <div class="field" style="top:191px">City</div>
  <div class="field" style="top:239px">Zip</div>
  <div class="field" style="top:288px">Phone</div>
  <div class="field" style="top:337px">*Email</div>
  <div class="field" style="top:382px;height:86px">Comments</div>
  <div class="btn" style="left:134px;top:482px;width:107px;height:45px">Submit</div>
</section>

<div class="reminder-photo" role="img" aria-label="Parents and children relaxing together on a living room floor"></div>
<div class="reminder">
  <div class="heading">Back to School Reminder</div>
  <div class="rule" style="margin-top:16px;width:54px"></div>
  <p>Most families see an uptick in morning “rush hour” activity once the school year begins, and so does your water heater. Can yours keep up with the increased demand? Contact us today for a water heater check-up and free quote on a replacement system.</p>
  <div class="btn" style="position:relative;margin-top:34px;width:185px;height:42px">Contact us today</div>
</div>

<section class="difference">
  <div class="copy">
    <div class="heading">The RT Difference Makers</div>
    <p>RT is a favorite choice among homeowners who appreciate our extensive range of home comfort and related services. Others like us best for our 100% satisfaction guarantee, while still others enjoy the many benefits that membership in our Preferred Service Club provides. Add it all up, and there’s a lot to like about RT Plumbing, Heating, AC &amp; Remodeling.</p>
    <div class="btn" style="position:relative;margin-top:30px;width:140px;height:44px">Learn More</div>
  </div>
  <div class="diff-photo" role="img" aria-label="Plumber in blue overalls fixing a kitchen faucet"></div>
</section>

<div class="savings-title"><div class="heading">Enjoy the savings… plus the added comfort!</div><div class="rule"></div></div>
<div class="offer" role="img" aria-label="Wall-mounted water heater" style="left:133px;background:linear-gradient(90deg,#dde2e8 45%,#b9c0c9)"><h3>New Water<br>Heater</h3><span class="save">Save $120</span><p>…on a new water heater, tank-style or tankless.</p></div>
<div class="offer" role="img" aria-label="Outdoor HVAC condenser units" style="left:452px;background:linear-gradient(90deg,#dbe7f1 45%,#a7b1bb)"><h3>HVAC<br>System</h3><span class="save">Save $350</span><p>…on a new heating or cooling system.</p></div>
<div class="offer" role="img" aria-label="Woman relaxing in a chair by a sunny window" style="left:769px;background:linear-gradient(90deg,#eef0ef 45%,#d8d6d0)"><h3>First-time<br>Customer</h3><span class="save">Save $35</span><p>…on any service we provide.</p></div>
<div class="btn" style="left:511px;top:3043px;width:178px;height:43px">Click for details</div>

<section class="blog">
  <div class="heading">Latest Blog<div class="rule"></div></div>
  <article class="post" style="left:133px"><div class="img" role="img" aria-label="Hands in gloves repairing a sink drain pipe"></div><div class="body"><div class="date">MAY 22, 2023</div><h4>Lorem Ipsum is simply dummy text of the printing</h4><p>Sed ut perspiciatis unde omnis iste natus error sit voluptatem accusantium doloremque laudantium, totam rem aperiam, eaque ipsa quae ab illo.</p></div><div class="btn">Read More</div></article>
  <article class="post" style="left:455px"><div class="img" role="img" aria-label="Plumber working under a sink"></div><div class="body"><div class="date">MAY 22, 2023</div><h4>Lorem Ipsum is simply dummy text of the printing</h4><p>Sed ut perspiciatis unde omnis iste natus error sit voluptatem accusantium doloremque laudantium, totam rem aperiam, eaque ipsa quae ab illo.</p></div><div class="btn">Read More</div></article>
  <article class="post" style="left:776px"><div class="img" role="img" aria-label="Technician adjusting a wall-mounted boiler"></div><div class="body"><div class="date">MAY 22, 2023</div><h4>Lorem Ipsum is simply dummy text of the printing</h4><p>Sed ut perspiciatis unde omnis iste natus error sit voluptatem accusantium doloremque laudantium, totam rem aperiam, eaque ipsa quae ab illo.</p></div><div class="btn">Read More</div></article>
  <div class="btn" style="left:511px;top:579px;width:178px;height:43px">Browse all posts</div>
</section>

<footer class="site-footer">
  <div class="fcol" style="left:133px;top:46px"><h5>About</h5><div class="rule"></div><ul><li>Company Profile</li><li>Guarantees &amp; Assurances</li><li>Preferred Service Club</li><li>Employment</li><li>Areas Served</li></ul></div>
  <div class="fcol" style="left:333px;top:46px"><h5>Plumbing</h5><div class="rule"></div><ul><li>Service &amp; Repair</li><li>Plumbing Installations</li><li>Outdoor Plumbing</li><li>Sewer &amp; Drain</li><li>Frozen Pipes</li><li>Gas Piping</li><li>Sump Pumps</li><li>Water Leak Detection &amp; Repair</li><li>Gas Piping</li></ul></div>
  <div class="fcol" style="left:603px;top:46px"><h5>Heating</h5><div class="rule"></div><ul><li>Preventive Maintenance</li><li>Boiler Service &amp; Repair</li><li>Furnace Service &amp; Repair</li><li>Boiler</li><li>Furnace</li><li>Gas Fireplace Insert</li><li>Ductless Air System</li><li>Combi-boiler</li></ul></div>
  <div class="fcol" style="left:869px;top:46px"><h5>Handy Work &amp; Remodeling</h5><div class="rule"></div><ul><li>Overview</li><li>Bathroom</li><li>Kitchens</li><li>Decks, Porches &amp; Patios</li><li>Basement</li><li>Windows &amp; Doors</li><li>Gas Fireplace</li><li>Interior &amp; Exterior</li><li>Handyman Services</li></ul></div>
  <div class="fcol" style="left:133px;top:293px"><h5>Water Heaters</h5><div class="rule"></div><ul><li>Service &amp; Repair</li><li>Tank-style Water Heater</li><li>Tankless Water Heater</li><li>Combi Boiler</li></ul></div>
  <div class="fcol" style="left:333px;top:293px"><h5>Air Conditioning</h5><div class="rule"></div><ul><li>Preventive Maintenance</li><li>Service &amp; Repair</li><li>New AC System</li><li>Ductless Air System</li></ul></div>
  <div class="fcol" style="left:603px;top:293px"><h5>Indoor Air Quality</h5><div class="rule"></div><ul><li>Air Cleaners</li><li>Duct Sealing</li><li>Humidity Control</li></ul></div>
  <div class="fcol" style="left:869px;top:293px"><h5>Commercial</h5><div class="rule"></div><ul><li>Plumbing</li><li>HVAC</li></ul></div>
  <div class="club"><div class="dot"></div><span>Preferred Service Club</span></div>
  <div class="address">18 Mill Pond Road<br>Ashford, MA 01790<br>555.210.4870 . 800.555.0143</div>
  <div class="follow">FOLLOW US <i></i></div>
  <div class="cards"><i></i><i></i><i></i><i></i></div>
  <div class="footer-line"></div>
  <div class="copyright">Copyright © 2023 All Rights Reserved</div>
</footer>

</body>
</html>
```